Quillmere NW Workshop Flyers

We need an editable template for a workshop flyer that fits our brand look and feel. It needs to include space for our speaker's pictures, date location, and registration information, a description of the event. The size needs to be 8 1/2 X 11 standard letter size. We have a sample flyer but are not happy with the color palette for the sample. We must be able to edit in MS Word or MS PPT to change the dates and descriptions.

• Must be in the brand color palate attached. Must be editable in MS Word or MS PPT. Must be 8/12 X11 standard letter size.

```html
<!DOCTYPE html>
<html lang="en">
<head>
<meta charset="utf-8">
<title>Quillmere NW Workshop Flyer</title>
<link href="https://fonts.googleapis.com/css2?family=Roboto+Condensed:wght@400;700&family=Source+Sans+3:wght@400;600;700&display=swap" rel="stylesheet">
<style>
  :root{
    --indigo:#3b407c;
    --indigo-deep:#33376e;
    --indigo-light:#51568f;
    --blue:#1a8fe3;
    --blue-bright:#1d98ec;
    --ink:#2b2b2b;
    --white:#ffffff;
    --stage:#ececef;
  }
  *{box-sizing:border-box;margin:0;padding:0}
  html,body{width:1200px;height:1200px;overflow:hidden;background:var(--stage)}
  .flyer{
    position:absolute;left:187px;top:20px;width:947px;height:1329px;
    transform:scale(0.8729);transform-origin:top left;
    background:var(--white);overflow:hidden;
    box-shadow:0 8px 30px rgba(0,0,0,.18);
    font-family:"Source Sans 3",sans-serif;color:var(--ink);
  }
  .hero{position:absolute;left:0;top:0;width:947px;height:367px;
    background:linear-gradient(100deg,#ffffff 0%,#ffffff 36%,#e9e4e6 48%,#c9a392 58%,#a9b3c8 68%,#d98a62 80%,#ef7a3c 92%,#e46a2c 100%);}
  .hero-rule{position:absolute;left:0;top:365px;width:947px;height:5px;background:var(--blue)}
  .brand{position:absolute;left:50px;top:150px;display:flex;align-items:center;gap:16px}
  .brand-dot{width:40px;height:40px;border-radius:50%;background:var(--indigo)}
  .brand-name{font-weight:700;font-size:40px;color:var(--indigo);letter-spacing:.3px}

  .intro{position:absolute;left:30px;top:378px;width:375px}
  .intro h1{font-family:"Roboto Condensed",sans-serif;font-weight:700;font-size:27px;line-height:38px;color:var(--indigo-deep);text-transform:uppercase}
  .intro h1 .accent{display:block;font-size:46px;line-height:47px;color:var(--blue);margin-top:2px}
  .intro p{font-size:18px;line-height:22.3px;text-align:justify;margin-top:9px;color:#262626}
  .intro p:first-of-type{margin-top:14px}

  .speaker{position:absolute;left:36px;width:380px;height:120px}
  .speaker-one{top:950px}.speaker-two{top:1092px}
  .speaker-photo{position:absolute;left:0;top:0;width:118px;height:118px;border-radius:50%;border:3px solid var(--blue);
    background:radial-gradient(circle at 50% 40%,#c99a7a,#6e4a35 70%)}
  .speaker-two .speaker-photo{background:radial-gradient(circle at 50% 45%,#b89478,#3e4c6a 70%)}
  .speaker-tag{position:absolute;left:116px;top:50px;width:196px;height:30px;background:var(--blue);
    clip-path:polygon(0 0,92% 0,100% 100%,0 100%);color:var(--white);font-weight:700;font-size:20px;line-height:30px;padding-left:20px}
  .speaker-name{position:absolute;left:133px;top:82px;font-weight:700;font-size:31px;color:#111;white-space:nowrap}

  .sessions{position:absolute;left:421px;top:323px;width:493px;height:940px;border-radius:28px 28px 0 0;
    background:linear-gradient(180deg,var(--indigo-light) 0%,var(--indigo) 60%,#3f447f 100%);color:var(--white);
    font-family:"Roboto Condensed",sans-serif}
  .session{position:absolute;left:27px;width:455px}
  .session-one{top:28px}
  .session-three{top:688px}
  .session h2{font-size:21px;font-weight:700;line-height:26px}
  .session .date{font-size:28px;font-weight:700;line-height:36px}
  .session h3{font-size:20px;font-weight:700;line-height:24px}
  .checks{list-style:none;margin-top:6px}
  .checks li{position:relative;padding-left:27px;font-size:17.8px;line-height:22.3px;margin-bottom:8.5px;text-align:left}
  .checks li.justified,.session-three .checks li{text-align:justify}
  .checks li::before{content:"";position:absolute;left:4px;top:3px;width:7px;height:13px;border:solid var(--blue-bright);border-width:0 3px 3px 0;transform:rotate(40deg)}
  .checks li.plain::before{display:none}
  .playbook{position:absolute;left:421px;top:905px;width:493px;height:85px;background:var(--blue-bright);color:var(--white);
    font-family:"Roboto Condensed",sans-serif;font-weight:700;font-size:28px;line-height:34px;padding:8px 0 0 53px}

  .footer{position:absolute;left:0;top:1270px;width:947px;height:59px;background:var(--blue-bright)}
  .footer-phone{position:absolute;left:0;top:1250px;width:330px;height:79px;background:linear-gradient(90deg,var(--indigo-light),var(--indigo-deep));
    clip-path:polygon(0 0,100% 0,91% 100%,0 100%);display:flex;align-items:center;padding-left:28px;gap:10px;color:var(--white);font-weight:700;font-size:33px}
  .footer-item{position:absolute;top:1285px;display:flex;align-items:center;gap:12px;color:var(--white);font-size:18.5px}
  .footer-mail{left:354px}.footer-web{left:700px}
</style>
</head>
<body>
<main class="flyer">
  <div class="hero" role="img" aria-label="Photo of many hands stacked together in a team huddle"></div>
  <div class="hero-rule"></div>
  <div class="brand"><span class="brand-dot"></span><span class="brand-name">Quillmere NW</span></div>

  <section class="intro">
    <h1>Are you interested in restorative practices in your school or district with <span class="accent">minimal scrapes and scratches?</span></h1>
    <p>Before any school can successfully implement restorative practices there is prep work to be done, data to be analyzed, mindset to be adjusted, and strategies and tools to adopt.</p>
    <p>Join a cohort of Michigan educators as they band together to explore, design, and implement restorative practices in their schools.</p>
    <p>In this three session seminar (9 hours total), participants will build their restorative toolkits over the course of seven weeks. They will pilot new tools, share challenges and successes and refine implementation with the guidance and support of experienced restorative practitioners.</p>
  </section>

  <div class="speaker speaker-one">
    <div class="speaker-photo" role="img" aria-label="Portrait photo of speaker Dana Whitfield"></div>
    <div class="speaker-tag">SPEAKERS</div>
    <div class="speaker-name">DANA WHITFIELD</div>
  </div>
  <div class="speaker speaker-two">
    <div class="speaker-photo" role="img" aria-label="Portrait photo of speaker Marcus Lund"></div>
    <div class="speaker-tag">SPEAKERS</div>
    <div class="speaker-name">MARCUS LUND</div>
  </div>

  <section class="sessions">
    <div class="session session-one">
      <h2>Building Your Restorative Toolkit Session 1:</h2>
      <div class="date">February 20, 2019 3:00PM to 6:00PM</div>
      <h3>Setting the Stage:</h3>
      <ul class="checks">
        <li>The Case for a Restorative Approach: Examine current realities and dive deep into data to name and change practices that do not benefit students.</li>
        <li>Restorative Justice: What it is and what it is not. Demystify a restorative approach.</li>
        <li>Address mindset to increase ease of adoption of a restorative approach: Walk in their shoes to examine the role that access and privilege plays in opportunity and outcome.<br>Building Your Restorative Toolkit Session 2: March 20, 2019 3:00PM to 6:00PM</li>
        <li class="plain">Circles and Beyond: Proactive restorative tools</li>
        <li>The 20 Minute Workout: Form support teams to problem-solve alternative approaches to punishment in 20 minute strength-based sessions.</li>
        <li class="justified">It's About Time (NOT!): Make time spent in reflection and In-school-suspension about outcomes and not about serving time.</li>
      </ul>
    </div>
    <div class="session session-three">
      <h2>Building Your Restorative Toolkit Session 3:</h2>
      <ul class="checks">
        <li>Walk the Path of Peace (get a free Calm Trail mat $49.00 value). Teach the talk of peace and walk that path.</li>
        <li>No More Tears with Tier One: Move the focus from students and their behaviors to staff and their capacity to incorporate best instructional and behavioral practices regardless of course content or subject matter.</li>
        <li>Referrals with a Twist: Replace outdated and ineffective referral forms with a reflective tool to support improved student and teacher relationships.</li>
      </ul>
    </div>
  </section>
  <div class="playbook">Receive The Circle Practice Guide free<br>($15.00 value)</div>

  <footer>
    <div class="footer"></div>
    <div class="footer-phone">
      <svg width="40" height="40" viewBox="0 0 24 24" aria-hidden="true"><path fill="#1d98ec" d="M6.6 10.8c1.4 2.8 3.8 5.1 6.6 6.6l2.2-2.2c.3-.3.7-.4 1-.2 1.1.4 2.3.6 3.6.6.6 0 1 .4 1 1V20c0 .6-.4 1-1 1C10.6 21 3 13.4 3 4c0-.6.4-1 1-1h3.5c.6 0 1 .4 1 1 0 1.3.2 2.5.6 3.6.1.3 0 .7-.2 1L6.6 10.8z"/></svg>
      <span>555 214 3098</span>
    </div>
    <div class="footer-item footer-mail">
      <svg width="34" height="22" viewBox="0 0 34 22" aria-hidden="true"><rect x="1" y="1" width="32" height="20" fill="none" stroke="#fff" stroke-width="2"/><path d="M1 1l16 12L33 1M1 21l12-10M33 21L21 11" fill="none" stroke="#fff" stroke-width="2"/></svg>
      <span>Dana.Whitfield@quillmerenw.com</span>
    </div>
    <div class="footer-item footer-web">
      <svg width="24" height="24" viewBox="0 0 24 24" aria-hidden="true"><g fill="none" stroke="#fff" stroke-width="1.6"><circle cx="12" cy="12" r="10"/><ellipse cx="12" cy="12" rx="4.5" ry="10"/><path d="M2 12h20M4 6.5h16M4 17.5h16"/></g></svg>
      <span>www.quillmereNW.com</span>
    </div>
  </footer>
</main>
</body>
</html>
```